LED Horticulture / Garden Grow Light Company Seeks Product & Company Brochure / Catalog

Verdant Beam Collective, LLC builds high intensity LED gardening / grow lights for horticulture. Greenhouse lighting, indoor gardening lighting and the hydroponics industry. The company is seeking a company brochure and/or catalog that features the product, The VBC 720 and a background on the company.

The company is also interested in using these layouts in templates for product packaging design such as standups in stores and box printing.

Target Market(s)

Indoor gardening industry and hobbyists, hydroponics supply stores, harlan's sprout boost, medical marijuana / cannabis cultivators and legal states such as Colorado.

Industry/Entity Type

It Company

Colors

Designer to choose colors to be used in the design.

Requirements
Must have
• Showcase the products / company and have a layout that can be incorporated amongst other printed marketing materials including packaging and catalogs. Competitors are the following: http://brivoxa.com https://www.tallowfinchled.com/ http://www.morventa.com/retail https://quibrel.science/ https://www.lumacrestled.com/

```html
<!DOCTYPE html>
<html lang="en">
<head>
<meta charset="utf-8">
<title>Verdant Beam Collective — Brochure Spread</title>
<link rel="stylesheet" href="https://fonts.googleapis.com/css2?family=Montserrat:ital,wght@0,400;0,500;0,700;1,800&display=swap">
<style>
  :root {
    --canvas-bg: #e6e6e6;
    --page-left: #ececec;
    --page-white: #ffffff;
    --green: #6cb83a;
    --green-deep: #3f9b2f;
    --green-light: #8cc43f;
    --text-dark: #3a3a3a;
    --text-body: #4a4a4a;
    --gutter-shadow: rgba(0,0,0,0.12);
    --panel-grey: #d9dcdc;
  }
  * { box-sizing: border-box; margin: 0; padding: 0; }
  html, body {
    width: 1200px; height: 1008px; overflow: hidden;
    background: var(--canvas-bg);
    font-family: "Montserrat", Arial, sans-serif;
  }
  .spread {
    position: absolute; left: 93px; top: 160px;
    width: 1012px; height: 681px;
    display: flex;
  }
  .page {
    position: relative; width: 506px; height: 681px; overflow: hidden;
  }
  .page--left {
    background: linear-gradient(to right, var(--page-left) 88%, #dedede 100%);
  }
  .page--right {
    background: linear-gradient(to right, #e2e2e2 0%, var(--page-white) 14%, var(--page-white) 70%, #f2f2f2 100%);
  }
  .page__header {
    position: absolute; left: 0; top: 0; width: 100%; height: 144px;
    background: var(--page-white);
  }
  .heading-block {
    position: absolute; left: 20px; top: 9px; width: 276px; height: 135px;
    background: linear-gradient(100deg, var(--green-deep), var(--green-light));
    border: 2px solid #5aa332;
    display: flex; align-items: center; padding-left: 36px;
  }
  .heading-block__title {
    color: #fff; font-weight: 800; font-style: italic;
    font-size: 46px; line-height: 1.0; text-align: center;
  }
  .brand {
    position: absolute; left: 318px; top: 22px; width: 170px;
    display: flex; flex-direction: column; align-items: center; gap: 10px;
  }
  .brand__mark {
    width: 70px; height: 70px; border-radius: 8px; background: var(--green);
  }
  .brand__name {
    color: var(--green-deep); font-weight: 700; font-size: 14px;
    line-height: 1.15; text-align: center;
  }
  .header-rule {
    position: absolute; left: 16px; right: 0; top: 142px; height: 3px;
    background: var(--green);
  }
  .body-copy {
    position: absolute; top: 170px;
    font-size: 8.4px; line-height: 12.2px; letter-spacing: -0.1px;
    color: var(--text-body); text-align: justify;
  }
  .body-copy--one p + p { margin-top: 12.2px; }
  .body-copy--one { left: 78px; width: 186px; }
  .body-copy--two { left: 274px; width: 190px; }
  .arrow-list { position: absolute; left: 16px; top: 407px; }
  .arrow-tab {
    position: absolute; left: 0; height: 52px;
    background: var(--green);
    clip-path: polygon(0 0, calc(100% - 26px) 0, 100% 50%, calc(100% - 26px) 100%, 0 100%);
    color: #fff; font-weight: 700; font-size: 20px;
    display: flex; align-items: center; padding-left: 46px;
  }
  .arrow-tab--one { top: 0; width: 306px; }
  .arrow-tab--two { top: 58px; width: 240px; }
  .arrow-tab--three { top: 114px; width: 251px; }
  .side-note {
    position: absolute; left: 288px; top: 472px; width: 176px;
    font-size: 14px; line-height: 17px; color: var(--text-dark); text-align: center;
  }
  .page-number {
    position: absolute; background: var(--green-light);
    color: #fff; font-weight: 700; font-size: 20px;
    display: flex; align-items: center; justify-content: center;
  }
  .page-number--left { left: 194px; top: 626px; width: 127px; height: 55px; }
  .page-number--right { left: 175px; top: 640px; width: 128px; height: 41px; }
  .heading-two {
    position: absolute; left: 19px; top: 68px;
    color: var(--green); font-weight: 800; font-style: italic; font-size: 47px;
  }
  .product-photo {
    position: absolute; left: 44px; top: 194px; width: 362px; height: 280px;
    background: linear-gradient(180deg, #e8eaea 0%, var(--panel-grey) 45%, #e4e6e6 100%);
    border-radius: 3px;
  }
  .product-reflection {
    position: absolute; left: 44px; top: 476px; width: 362px; height: 80px;
    background: linear-gradient(180deg, rgba(200,204,204,0.45), rgba(255,255,255,0));
  }
  .caption {
    position: absolute; left: 96px; top: 584px; width: 260px;
    font-size: 10.5px; line-height: 13px; color: var(--text-body); text-align: center;
  }
  .gutter {
    position: absolute; left: 496px; top: 0; width: 20px; height: 681px;
    background: linear-gradient(to right, rgba(0,0,0,0), var(--gutter-shadow), rgba(0,0,0,0));
  }
</style>
</head>
<body>
  <main class="spread">
    <section class="page page--left">
      <div class="page__header"></div>
      <div class="heading-block"><h1 class="heading-block__title">Heading<br>One</h1></div>
      <div class="brand">
        <span class="brand__mark"></span>
        <span class="brand__name">Verdant Beam<br>Collective</span>
      </div>
      <div class="header-rule"></div>

      <div class="body-copy body-copy--one">
        <p>Acepedit odici doluptam, sit harum quia natatibus volori di quatur, offici odipicias sitatem exerovi tiisseque pliquos toritibus quiderspis es apid quissin vellam nam eostisc ieturestrum quo blabo. Nem eum quam ne nam as et od quiatentias</p>
        <p>eum inverfe riatur aute nonest ma net laut lacearchic te vel molenisto eveles sit harcid et, volupicius con prorest que none volum atiberio verio ent ommodi dolo excepra ipsae molores ectoreiciur aut am restibeatur reperib usandem hicia expellant opta dolut ipsa dolo mos ut expliqua-</p>
      </div>
      <div class="body-copy body-copy--two">
        <p>sin cust, essint por autecta tessequam nosseque atis in reptat reptae nos acepudam soluptam quam de ne cum nus dolupta dolesto beaque corrum, sam lit apeditati dollabo ribust, inis ra culpa volorit hario. Ucipidiassum sum eaquia volupti onsequa spernam aut etur seque velentis essequo doluptturis es dis numque la que sitatestem quam, ad moluptatur as et ma et as alit lant evel ium que remporatem eos aut mosantis et ent eseceatem qui unt.</p>
        <p>Caboriberum facessectas des exerferia nisqui ut vendis eveles andant, iuntiure quis aliquam reped ut am</p>
      </div>

      <div class="arrow-list">
        <div class="arrow-tab arrow-tab--one">Lorem Ipsum</div>
        <div class="arrow-tab arrow-tab--two">Lorem Ipsum</div>
        <div class="arrow-tab arrow-tab--three">Lorem Ipsum</div>
      </div>
      <p class="side-note">Iniminveles comni offictem qui debit ratum fuga.<br>Igeni dionser isquam</p>
      <div class="page-number page-number--left">002</div>
    </section>

    <section class="page page--right">
      <h2 class="heading-two">Heading Two</h2>
      <div class="product-photo" role="img" aria-label="Photograph of the VBC 720 LED grow light: four square LED boards on a silver frame"></div>
      <div class="product-reflection"></div>
      <p class="caption">Iniminveles comni offictem qui debit ratum fuga. Igeni dionser isquam fuga. Borrum nis dernatur, et dolupti stemporest.</p>
      <div class="page-number page-number--right">003</div>
    </section>
    <div class="gutter"></div>
  </main>
</body>
</html>
```